Update patient consent forms and contract

Objective
Redesign the existing patient contract information document to create a modern,contempory, and easy-to-understand experience for patients. The updated design should improve readability, accessibility, and overall presentation while maintaining compliance with healthcare and legal requirements.

Key Deliverables

Refreshed visual design and layout
Improved information hierarchy and readability
Modern typography and colour palette aligned with brand guidelines
Clear section headings and navigation
Print-ready and digital versions (PDF)

Include KEV Logo within patient KEV consent to treatment. Ideally this document should be portrait not landscape.
Updates

I would love a front page to be included in the document

```html
<!DOCTYPE html>
<html lang="en">
<head>
<meta charset="utf-8">
<title>Lark Orthodontics – Consent to Treatment</title>
<link rel="stylesheet" href="https://fonts.googleapis.com/css2?family=Montserrat:wght@300;400;600;700&display=swap">
<style>
  :root {
    --navy: #1b2340;
    --ink: #4a4a4f;
    --rule: #8a8a8e;
    --mark-grey: #7d7d7d;
    --photo-light: #ece6dc;
    --photo-mid: #d9d2c6;
    --photo-blue: rgba(156,196,228,.55);
    --paper: #ffffff;
  }
  * { box-sizing: border-box; margin: 0; padding: 0; }
  html, body { width: 848px; height: 1200px; overflow: hidden; background: var(--paper); }
  body { font-family: "Montserrat", sans-serif; color: var(--ink); position: relative; }

  .hero-photo {
    position: absolute; left: 0; top: 0; width: 848px; height: 292px;
    background: linear-gradient(100deg, var(--photo-mid) 0%, var(--photo-light) 35%, #f3efe8 55%, var(--photo-light) 75%, var(--photo-mid) 100%);
  }
  .hero-photo::after {
    content: ""; position: absolute; inset: 0;
    background: radial-gradient(ellipse 90px 60px at 360px 190px, var(--photo-blue), transparent 70%);
  }

  .brand {
    position: absolute; left: 170px; top: 400px;
    display: flex; align-items: center; gap: 14px;
  }
  .brand-dot { width: 44px; height: 44px; border-radius: 50%; background: var(--mark-grey); }
  .brand-name { font-size: 30px; font-weight: 400; color: var(--navy); line-height: 1; }

  .block { position: absolute; width: 250px; font-size: 10.3px; line-height: 12.9px; font-weight: 300; letter-spacing: -0.15px; }
  .block p { text-align: justify; hyphens: auto; }
  .heading { font-size: 10.8px; font-weight: 700; color: var(--navy); line-height: 12.9px; letter-spacing: 0; }
  .label { font-weight: 600; color: var(--navy); letter-spacing: 0; }
  .field-line { display: inline-block; border-bottom: 0.8px solid var(--ink); height: 8px; }
  .tight { letter-spacing: -0.8px; white-space: nowrap; }

  .option { display: flex; gap: 4px; align-items: flex-start; }
  .box { width: 7px; height: 7px; border: 1px solid var(--navy); margin-top: 3px; flex: none; box-shadow: 1px 1px 0 var(--navy); }
  .indent { padding-left: 12px; }
  .bank p { text-align: left; }

  .footer-rule { position: absolute; left: 85px; width: 678px; height: 1px; background: var(--rule); }
  .footer-rule::before, .footer-rule::after {
    content: ""; position: absolute; top: -2px; width: 5px; height: 5px; border-radius: 50%; background: var(--rule);
  }
  .footer-rule::before { left: -2px; } .footer-rule::after { right: -2px; }
  .contact {
    position: absolute; left: 85px; width: 678px; top: 1048px;
    display: flex; justify-content: space-between; font-size: 10.2px; font-weight: 300;
  }
  .contact b { font-weight: 700; color: var(--navy); }
  .practitioners-title { position: absolute; left: 85px; top: 1087px; font-size: 10.8px; font-weight: 700; color: var(--navy); }
  .practitioner { position: absolute; top: 1113px; font-size: 10.2px; line-height: 13px; font-weight: 300; }
  .practitioner strong { display: block; font-weight: 700; color: var(--navy); font-size: 10.8px; }
</style>
</head>
<body>
  <div class="hero-photo" role="img" aria-label="Photo of orthodontists in white coats examining a patient in the chair"></div>

  <div class="brand"><span class="brand-dot"></span><span class="brand-name">KEV</span></div>

  <!-- left column -->
  <div class="block heading" style="left:155px;top:542px">CONSENT TO TREATMENT</div>
  <div class="block" style="left:155px;top:568px"><span class="label">Patient Name:</span> <span class="field-line" style="width:158px"></span></div>
  <div class="block heading" style="left:155px;top:594px">Thank you for choosing Lark Orthodontics.</div>
  <div class="block" style="left:155px;top:620px"><p>To assist with managing your treatment fees, please select your preferred payment method below. If you would prefer to pay at each scheduled appointment, please advise our reception team. Please note that appointments are generally scheduled every 6–8 weeks.</p></div>
  <div class="block heading" style="left:155px;top:710px">Please select one option:</div>
  <div class="block" style="left:155px;top:735px">
    <div class="option"><span class="box"></span><span class="heading">Credit Card Direct Debit</span></div>
    <p class="indent">I would like to pay via credit card direct debit.</p>
  </div>
  <div class="block" style="left:155px;top:774px"><p>I understand that Lark Orthodontics will send me a secure PayLink payment link to enter my credit-card details. The card provided will be securely stored and used as my nominated payment method for future scheduled payments relating to my treatment plan.</p></div>
  <div class="block heading" style="left:155px;top:864px">Monthly Direct Bank Transfer</div>
  <div class="block" style="left:155px;top:889px"><p class="tight">I would like to pay via monthly direct bank transfer.</p></div>
  <div class="block" style="left:155px;top:915px">
    <div class="option"><span class="box"></span><p>I understand that I am responsible for ensuring monthly payments are made on time in accordance with my agreed payment arrangement.</p></div>
  </div>

  <!-- right column -->
  <div class="block heading" style="left:444px;top:542px">Important</div>
  <div class="block" style="left:444px;top:568px"><p>When making direct transfer payments, please use the patient’s full name as the payment reference (for example: Emily Smith), rather than the account holder’s name. This ensures payments are correctly allocated to your treatment account.</p></div>
  <div class="block heading" style="left:444px;top:671px">Patient Declaration</div>
  <div class="block" style="left:444px;top:697px"><p>I have read and understood the payment options above and agree to my selected payment method.</p></div>
  <div class="block" style="left:444px;top:774px"><span class="label">Signature:</span> <span class="field-line" style="width:185px"></span></div>
  <div class="block" style="left:444px;top:825px"><span class="label">Date:</span> <span class="field-line" style="width:141px"></span></div>
  <div class="block heading" style="left:444px;top:876px">Our bank account details:</div>
  <div class="block bank" style="left:444px;top:902px">
    <p><span class="label">Account Name:</span> Lark Orthodontics</p>
    <p><span class="label">Bank</span>: Southbank Mutual</p>
    <p><span class="label">BSB:</span> 012 345</p>
    <p><span class="label">Account Number:</span> 12345678</p>
  </div>

  <div class="footer-rule" style="top:1040px"></div>
  <div class="contact">
    <span>48 Wattle Grove Rd, Elmvale VIC 3190</span><span>/</span>
    <span><b>T</b>. 03 9000 1234</span><span>/</span>
    <span><b>F.</b> 03 9000 5678</span><span>/</span>
    <span><b>E</b>. elmvale@lark-ortho.com.au</span>
  </div>
  <div class="footer-rule" style="top:1070px"></div>

  <div class="practitioners-title">Registered Specialist Orthodontists</div>
  <div class="practitioner" style="left:85px"><strong>Dr. Hannah Brierly</strong>MDSc, Grad Dip Clin Dent, BDSc(Hons)</div>
  <div class="practitioner" style="left:307px"><strong>Dr. Marco Lentini</strong>MDSc, Grad Dip Clin Dent, MOrth, BDSc</div>
  <div class="practitioner" style="left:537px"><strong>Dr. Samuel Okoro</strong>DCD, MOrth, MRACDS Orth), BDSc (Hons)</div>
</body>
</html>
```